Home page design for community learning promoters' website

There are about 3,000 community learning centers where people from underprivileged / marginalized communities can learn about basic technology topics like: how to use computers, how to use Internet (create an email, join and use social networks, etc.), how to use Word, Excel, PowerPoint, and so on... This is very useful for them because it gives them opportunities to find / get a better job and improve their standard of living.

Well, this website is an online community for those men and women (the promoters) who are responsible for leading the centers. They coordinate all the activities in the centers and they teach their students.

The website has two main objectives: 1) create culture about the importance of the promoters role in their communities and 2) create a place where promoters can learn, take online courses and share best practices.

The first objective is the "public" part of the website (homepage and public information) and the second one is the "private" part which is a pinwheel like online community (accessible only for registered users).

What we need is a fresh and modern visual design for 1) "public" homepage and 2) "private" homepage. I am attaching some mockups for the homepage "public" part (two different options) and for the main page of the "private" part (the pinwheel like online community). This doesn't mean that your design should be like those mockups, but they could be a guide for you to get ideas and better understend the website objectives. What we need is innovation.

The project scope is to design the home page for the "public" part and the home page for the "private" part. If you have any question, please ask me.

Target Market(s)

Target market (promoters) are 20-40 years old, they work from 4 to 8 hours in the centers and their connections are mainly satellital 256Kb/s

Industry/Entity Type

Internet

Requirements
Must have
• Spanish labeling. Find below what homepage must have. I include english / spanish versions. For sample text you can use "lorem ipsum". If you need help with spanish tranlations you can ask me.

The homepage must have:

Links / menu to main sections:
- Who we are / Quiénes somos
- What we do / Qué hacemos
- Our impact / Nuestro impacto
- Enter now! / ¡Ingresa ahora!

Benefits that the site offer to the promoters (why they should join the online community). Call-to-action should be "Join now / Regístrate ahora"
- Get trained (Take online courses and get access to more than 450 learning resources) / Capacítate (Toma cursos en línea y accede a más de 450 recursos de aprendizaje)
- Get certified (Approve the course and become a certified promoter) / Certifícate (Aprueba el curso y conviértete en un promotor certificado)
- Connect (Connect and work with more than 3,000 promoters around the country) / Conéctate (Conéctate y colabora con más de 3,000 promotores de todo el país)
- Share (Learn and share information with other promoters) / Comparte (Aprende y comparte información con otros promotores)

Links / blocks / menus to secondary sections:
- Success stories / Historias de éxito
- Events and contests / Concursos y eventos
- News or Featured news / Noticias destacadas
- Follow us on... (social networks like pinwheel, glimmo, quorvaSt, etc.) / Síguenos en...
- Frequently asked questions / Preguntas frecuentes
- Contact us / Contáctanos
- Site map / Mapa del sitio
- Privacy policy / Políticas de privacidad
- Terms and conditions of use / Términos y condiciones de uso

Also should include statistics like:
- More that 3,000 promoters / Más de 3,000 promotores
- More than 850 learning resources / Más de 850 recursos de aprendizaje
- More than 450,000 students / Más de 450,000 estudiantes

```html
<!DOCTYPE html>
<html lang="es">
<head>
<meta charset="utf-8">
<title>Enlaza — Comunidad de promotores</title>
<link href="https://fonts.googleapis.com/css2?family=Source+Sans+3:wght@300;400;600;700&display=swap" rel="stylesheet">
<style>
  :root{
    --blue-top:#3fa4e6;
    --blue-bottom:#1d78c8;
    --blue-text:#2f7bc4;
    --orange-top:#ff9a2a;
    --orange-bottom:#f26a07;
    --grey-text:#555555;
    --icon-grey:#a9a9a9;
    --hero-bg:#efefef;
    --subnav-top:#f3f3f3;
    --subnav-bottom:#d9d9d9;
    --footer-bg:#333333;
    --footer-bottom:#232323;
    --white:#ffffff;
    --quote-bg:#1c1c1c;
    --arrow:#f58a12;
  }
  *{box-sizing:border-box;margin:0;padding:0}
  html,body{width:1052px;height:1200px;overflow:hidden;background:var(--white)}
  body{font-family:"Source Sans 3","Source Sans Pro",Arial,sans-serif;position:relative;color:var(--grey-text)}
  a{color:inherit;text-decoration:none}

  .topbar{position:absolute;left:0;top:0;width:1052px;height:62px;background:linear-gradient(var(--blue-top),var(--blue-bottom))}
  .brand{position:absolute;left:106px;top:12px;font-size:30px;font-weight:700;color:var(--white);line-height:36px;white-space:nowrap}
  .main-nav{position:absolute;left:296px;top:0;height:62px;display:flex;align-items:center;white-space:nowrap}
  .main-nav a{color:var(--white);font-weight:600;font-size:14px;padding:0 16px;border-left:1px solid rgba(255,255,255,.25);line-height:26px}
  .main-nav a:first-child{border-left:none}
  .btn{display:flex;align-items:center;justify-content:center;color:var(--white);font-weight:700;border-radius:20px;background:linear-gradient(var(--orange-top),var(--orange-bottom));box-shadow:0 2px 3px rgba(0,0,0,.25);white-space:nowrap;overflow:hidden}
  .btn-community{position:absolute;left:742px;top:13px;width:208px;height:37px;font-size:14px}

  .subnav{position:absolute;left:0;top:62px;width:1052px;height:47px;background:linear-gradient(var(--subnav-top),var(--subnav-bottom));border-bottom:2px solid #c9c9c9;display:flex;align-items:center;padding-left:92px;white-space:nowrap}
  .subnav a{font-size:15px;font-weight:600;color:#5a5a5a;padding:0 20px;border-left:1px solid #c4c4c4;line-height:24px}
  .subnav a:first-child{border-left:none;padding-left:16px}

  .hero{position:absolute;left:0;top:109px;width:1052px;height:345px;background:var(--hero-bg)}
  .hero h1{position:absolute;left:0;top:44px;width:1052px;text-align:center;font-size:38px;font-weight:600;line-height:52px;letter-spacing:.3px;color:var(--grey-text);white-space:nowrap}
  .stat{position:absolute;top:202px;text-align:center;white-space:nowrap}
  .stat .row{display:flex;align-items:center;justify-content:center;gap:10px}
  .stat .plus{font-size:28px;font-weight:600;color:#333;margin-left:6px}
  .stat .num{font-size:38px;font-weight:700;color:var(--blue-text);line-height:44px}
  .stat .label{font-size:20px;font-weight:700;color:var(--grey-text);letter-spacing:.5px;line-height:24px;margin-top:4px}
  .stat-divider{position:absolute;top:207px;height:74px;border-left:2px dashed #9a9a9a}

  .faces{position:absolute;left:169px;top:481px;width:684px;height:238px;display:grid;grid-template-columns:repeat(6,114px);grid-template-rows:repeat(2,119px)}
  .face{width:114px;height:119px}
  .quote{background:var(--quote-bg);color:var(--white);padding:8px 9px;font-size:10px;line-height:12.5px;font-weight:600;overflow:hidden}
  .quote cite{display:block;font-style:normal;font-weight:700;margin-top:8px}
  .arrow{position:absolute;top:578px}

  .join-title{position:absolute;left:0;top:768px;width:1052px;text-align:center;font-size:26px;font-weight:400;color:#333;white-space:nowrap}
  .benefit{position:absolute;top:840px;width:140px;text-align:center;white-space:nowrap}
  .benefit h3{font-size:14px;font-weight:700;color:var(--blue-text);letter-spacing:.3px}
  .benefit svg{display:block;margin:14px auto 0}
  .btn-register{position:absolute;left:708px;top:880px;width:198px;height:41px;font-size:15px}

  .footer{position:absolute;left:0;top:971px;width:1052px;height:171px;background:var(--footer-bg);color:var(--white)}
  .footer-col{position:absolute;top:24px;font-size:12px;line-height:21px;white-space:nowrap}
  .footer-col h4{font-size:12px;font-weight:600;text-transform:uppercase;margin-bottom:2px}
  .footer-col .active{color:var(--arrow)}
  .legal{position:absolute;left:0;top:1142px;width:1052px;height:58px;background:var(--footer-bottom);color:var(--white);text-align:center;font-size:12px;padding-top:8px;line-height:21px;white-space:nowrap}
  .legal nav a{margin:0 6px}
</style>
</head>
<body>

<header class="topbar">
  <div class="brand">Enlaza</div>
  <nav class="main-nav">
    <a href="#">Quiénes Somos</a>
    <a href="#">Qué Hacemos</a>
    <a href="#">Nuestro Impacto</a>
  </nav>
  <a class="btn btn-community" href="#">ENTRAR A LA COMUNIDAD</a>
</header>

<nav class="subnav">
  <a href="#">Historias de Éxito</a>
  <a href="#">Eventos y Concursos</a>
  <a href="#">Noticias Destacadas</a>
</nav>

<section class="hero">
  <h1>LOS PROMOTORES SON HOMBRES Y MUJERES<br>QUE QUIEREN MEJORAR A MÉXICO</h1>

  <div class="stat" style="left:120px;width:210px">
    <div class="row">
      <svg width="68" height="52" viewBox="0 0 68 52" aria-hidden="true">
        <g fill="var(--icon-grey)">
          <circle cx="18" cy="16" r="9"/><path d="M2 48c0-14 7-20 16-20s16 6 16 20z"/>
          <circle cx="50" cy="16" r="9"/><path d="M34 48c0-14 7-20 16-20s16 6 16 20z"/>
          <circle cx="34" cy="11" r="10"/><path d="M14 50c0-16 9-24 20-24s20 8 20 24z" stroke="var(--hero-bg)" stroke-width="2"/>
        </g>
      </svg>
      <span class="plus">+</span><span class="num">3000</span>
    </div>
    <div class="label">PROMOTORES</div>
  </div>
  <div class="stat-divider" style="left:361px"></div>

  <div class="stat" style="left:400px;width:190px">
    <div class="row">
      <svg width="50" height="50" viewBox="0 0 50 50" aria-hidden="true">
        <g fill="none" stroke="var(--icon-grey)" stroke-width="2.5">
          <path d="M4 8h22l8 8v30H4z"/><path d="M16 4h22l8 8v30"/>
          <path d="M10 22h18M10 28h18M10 34h18M10 40h12"/>
        </g>
      </svg>
      <span class="plus">+</span><span class="num">800</span>
    </div>
    <div class="label">PUBLICACIONES</div>
  </div>
  <div class="stat-divider" style="left:620px"></div>

  <div class="stat" style="left:660px;width:260px">
    <div class="row">
      <svg width="60" height="50" viewBox="0 0 60 50" aria-hidden="true">
        <g fill="var(--icon-grey)">
          <path d="M30 6 58 18 30 30 2 18z"/>
          <path d="M14 26v12c0 6 8 9 16 9s16-3 16-9V26L30 33z"/>
          <rect x="52" y="18" width="2" height="14"/>
        </g>
      </svg>
      <span class="plus">+</span><span class="num">450,000</span>
    </div>
    <div class="label">ALUMNOS</div>
  </div>
</section>

<svg class="arrow" style="left:104px" width="24" height="44" viewBox="0 0 24 44" aria-hidden="true"><path d="M21 2 3 22l18 20" fill="none" stroke="var(--arrow)" stroke-width="3"/></svg>

<section class="faces">
  <div class="face" role="img" aria-label="Retrato de promotora sonriente" style="background:linear-gradient(#f3e6d6,#d9b48a)"></div>
  <div class="face" role="img" aria-label="Retrato de promotor con traje" style="background:linear-gradient(#f1e9e2,#8c6f5e)"></div>
  <div class="face" role="img" aria-label="Retrato de promotora con lentes" style="background:linear-gradient(#cfc0a8,#b08f72)"></div>
  <div class="face" role="img" aria-label="Retrato de promotor con traje" style="background:linear-gradient(#f4f4f4,#6b625c)"></div>
  <div class="face" role="img" aria-label="Retrato de promotora de cabello oscuro" style="background:linear-gradient(#e9dfd8,#5b3b2d)"></div>
  <div class="face" role="img" aria-label="Retrato de promotor pensativo" style="background:linear-gradient(#f5f5f5,#b89a85)"></div>
  <div class="face" role="img" aria-label="Retrato de promotor con traje oscuro" style="background:linear-gradient(#f3f3f3,#4a4240)"></div>
  <div class="face" role="img" aria-label="Retrato de promotora rubia" style="background:linear-gradient(#a9a88c,#d7c09a)"></div>
  <div class="face" role="img" aria-label="Retrato de promotor con lentes" style="background:linear-gradient(#f1f1f1,#7d99b8)"></div>
  <div class="face quote">“Lorem ipsum dolor sit amet, consectetur adipiscing elit. Curabitur eget rhoncus justo.”<cite>Lucía Moreno</cite></div>
  <div class="face" role="img" aria-label="Retrato de promotor sonriente" style="background:linear-gradient(#7a5a3c,#c9a98a)"></div>
  <div class="face" role="img" aria-label="Retrato de promotora pelirroja" style="background:linear-gradient(#f4f4f4,#b86a45)"></div>
</section>

<svg class="arrow" style="left:900px" width="24" height="44" viewBox="0 0 24 44" aria-hidden="true"><path d="M3 2l18 20L3 42" fill="none" stroke="var(--arrow)" stroke-width="3"/></svg>

<h2 class="join-title">Si eres promotor, únete a la comunidad virtual de aprendizaje</h2>

<div class="benefit" style="left:122px">
  <h3>CAPACÍTATE</h3>
  <svg width="76" height="64" viewBox="0 0 76 64" aria-hidden="true">
    <g fill="var(--icon-grey)">
      <circle cx="26" cy="12" r="8"/>
      <path d="M14 24h20l16-8 3 5-17 11v14H14z"/>
      <rect x="30" y="34" width="18" height="28"/>
      <rect x="18" y="46" width="8" height="16"/>
    </g>
    <path d="M52 18 70 2" stroke="var(--icon-grey)" stroke-width="3"/>
  </svg>
</div>
<div class="benefit" style="left:266px">
  <h3>CERTIFÍCATE</h3>
  <svg width="76" height="64" viewBox="0 0 76 64" aria-hidden="true">
    <g fill="none" stroke="var(--icon-grey)" stroke-width="5" stroke-linecap="round">
      <circle cx="24" cy="22" r="14"/>
      <path d="M34 32 58 54M16 34l-6 24M58 54c8 2 12-6 6-10-5-3-10 2-6 6"/>
    </g>
  </svg>
</div>
<div class="benefit" style="left:414px">
  <h3>CONÉCTATE</h3>
  <svg width="76" height="64" viewBox="0 0 76 64" aria-hidden="true">
    <g fill="none" stroke="var(--icon-grey)" stroke-width="5" stroke-linecap="round">
      <path d="M6 24a46 46 0 0 1 64 0M16 35a32 32 0 0 1 44 0M27 46a16 16 0 0 1 22 0"/>
    </g>
    <circle cx="38" cy="56" r="5" fill="var(--icon-grey)"/>
  </svg>
</div>
<div class="benefit" style="left:564px">
  <h3>COMPARTE</h3>
  <svg width="76" height="64" viewBox="0 0 76 64" aria-hidden="true">
    <g fill="var(--icon-grey)"><circle cx="52" cy="12" r="9"/><circle cx="24" cy="32" r="9"/><circle cx="52" cy="52" r="9"/></g>
    <path d="M52 12 24 32l28 20" fill="none" stroke="var(--icon-grey)" stroke-width="4"/>
  </svg>
</div>

<a class="btn btn-register" href="#">¡REGÍSTRATE AHORA!</a>

<footer class="footer">
  <div class="footer-col" style="left:107px">
    <h4>Sobre nosotros</h4>
    <div>- &nbsp;Qué Hacemos</div>
    <div>- &nbsp;<span class="active">Quiénes Somos</span></div>
    <div>- &nbsp;Nuestro Impacto</div>
  </div>
  <div class="footer-col" style="left:268px">
    <h4>Involúcrate</h4>
    <div>- Historias de éxito</div>
    <div>- Eventos y concursos</div>
    <div>- Noticias</div>
  </div>
  <div class="footer-col" style="left:438px">
    <h4>Más información</h4>
    <div>- Preguntas frecuentes</div>
    <div>- Contáctanos</div>
  </div>
  <div class="footer-col" style="left:720px">
    <h4>Contacto información</h4>
    <div>Dirección: Lorem ipsum #1234 DF, México</div>
    <div>Teléfono: 123 456-7890</div>
    <div>Fax: 123 456 7899</div>
    <div>E-Mail: soporte@redaprende.example</div>
  </div>
</footer>

<div class="legal">
  <div>Copyright © 2013. Red Aprende</div>
  <nav><a href="#">Políticas de privacidad</a><a href="#">Términos y condiciones de uso</a><a href="#">Mapa del sitio</a></nav>
</div>

</body>
</html>
```